Newsletter/Flyer/Advertisement - ("Call for Papers") Design Project

We will be arranging a conference on electronics integration technology in Helsinki, Finland in September 2014 and we would need catchy looking information leaflet to advertise it. We call this a “call for papers” and it is distributed to all potential attendants of the conference. I have attached the plain text part as a MS Word document “1st Call for Papers.docx”. The title format, font etc. can be changed and modified but the 1/2/1 column layout should remain the same and the text should not extend to third page.
There are 5 logos that must be included; the event logo KVRD2014 should be on the front page but the remaining 4 logos (Brenmoor University, OQJU, LDSW, and uNOLT) should be placed in the bottom footer of both pages. I have attached the call for papers from the previous KVRD conference (in 2012) as a reference of how it has looked before. However, I would like to make it visually little bit more like the GYPB call for papers, which is also attached. If you can find a little "flavor" perhaps from the theme of the conference (electronics) and/or something local (Helsinki) to make it stand out next to the old KVRD one. I think the theme of electronics is quite universal but I will also attach some photos of Helsinki.
Please do not hesitate to ask for clarifications!
Updates

Target Market(s)

Technical people and academics around the world

Industry/Entity Type

Electronics

Requirements
Must have
• Texh included in the "1st Call for Papers.docx". 5 logos: the KVRD2014 event logo somewhere up in the front; Brenmoor University, OQJU, LDSW, and uNOLT logos down in the bottom footer (in this particular order).
Nice to have
• Some local "flavor" from Helsinki and the theme of the conference (microelectronics) present in the appearance.

```html
<!DOCTYPE html>
<html lang="en">
<head>
<meta charset="utf-8">
<title>KVRD 2014 – First Call for Papers</title>
<link href="https://fonts.googleapis.com/css2?family=Russo+One&family=Lato:ital,wght@0,400;0,700;0,900;1,400;1,900&display=swap" rel="stylesheet">
<style>
  :root{
    --bg:#8a8a88;
    --paper:#ffffff;
    --navy:#1c3a86;
    --navy-dark:#132a66;
    --link:#2a4fa8;
    --ink:#2b2b2b;
    --tab-top:#f2f2f2;
    --tab-bottom:#c9cbcf;
    --night-1:#0d2150;
    --night-2:#2f58a3;
    --lights:#c98a3c;
    --city-1:#e9e9e9;
    --city-2:#7d7d7d;
  }
  *{box-sizing:border-box;margin:0;padding:0}
  html,body{width:1200px;height:801px;overflow:hidden}
  body{background:var(--bg);font-family:"Lato",sans-serif;color:var(--ink);position:relative}
  .page{position:absolute;top:18px;width:540px;height:765px;background:var(--paper);overflow:hidden;box-shadow:0 4px 14px rgba(0,0,0,.35)}
  .page--front{left:40px}
  .page--back{left:620px}
  p{font-size:9.4px;line-height:1.3}

  /* front header */
  .hero{height:140px;background:linear-gradient(180deg,var(--night-1) 0%,var(--night-2) 55%,var(--lights) 82%,#3a2a1c 100%)}
  .event-mark{position:absolute;left:30px;top:0;width:92px;height:96px;background:#fff;clip-path:polygon(0 0,100% 0,100% 100%,50% 86%,0 100%);display:flex;align-items:center;justify-content:center;gap:4px}
  .event-mark__dot{width:8px;height:8px;background:var(--navy)}
  .event-mark__name{font-family:"Lato",sans-serif;font-weight:900;font-size:14px;color:var(--navy)}
  .title-band{background:linear-gradient(180deg,var(--navy) 0%,var(--navy-dark) 100%);text-align:center;padding:12px 10px 8px;color:#fff}
  .title-band h1{font-family:"Russo One",sans-serif;font-size:33px;font-weight:400;letter-spacing:1px;text-shadow:2px 2px 2px rgba(0,0,0,.45)}
  .title-band h2{font-family:"Lato",sans-serif;font-weight:900;font-size:12.5px;font-variant:small-caps;letter-spacing:.3px;margin-top:5px}
  .event-date{text-align:center;color:var(--navy);font-weight:900;font-size:16px;margin-top:7px}
  .event-url{text-align:center;color:var(--link);font-size:8.5px;margin-bottom:4px}
  .intro{font-style:italic;padding:0 22px;font-size:9px}

  .columns{display:flex;gap:14px;padding:4px 22px 0}
  .col{flex:1}
  .tab{display:inline-block;background:linear-gradient(180deg,var(--tab-top),var(--tab-bottom));color:var(--navy);font-weight:900;font-size:13px;padding:3px 14px 3px 6px;box-shadow:2px 2px 3px rgba(0,0,0,.3);margin:6px 0 6px -6px}
  .topic{color:var(--navy);font-weight:700;font-size:10px;margin:6px 0 2px}
  .col p{text-align:justify}

  .partners{position:absolute;left:0;right:0;bottom:0;height:74px;display:flex;align-items:center;justify-content:space-around;padding:0 20px}
  .partner{display:flex;align-items:center;gap:5px;font-weight:900;font-size:17px;color:var(--navy)}
  .partner__mark{width:11px;height:11px;border-radius:50%;background:var(--navy)}

  /* back */
  .back-top{padding:14px 18px 0}
  .band-welcome{position:absolute;left:0;right:0;top:448px;height:64px;background:var(--navy);color:#fff;text-align:center;font-style:italic;font-weight:900;font-size:14.5px;line-height:1.35;padding-top:11px}
  .chairs{position:absolute;left:0;right:0;top:522px;display:flex;justify-content:space-around;text-align:center}
  .chair__name{color:var(--navy);font-weight:900;font-style:italic;font-size:11px}
  .chair__role{font-size:11px;margin-top:5px}
  .cityscape{position:absolute;left:0;right:0;bottom:0;height:185px;background:linear-gradient(180deg,#fff 0%,var(--city-1) 25%,var(--city-2) 75%,#555 100%)}
  .dates li{list-style:none;font-size:9.4px;margin:6px 0 0 6px}
  .dates li::before{content:"";display:inline-block;width:5px;height:5px;border-radius:50%;background:var(--navy);margin-right:4px;vertical-align:middle}
  .dates b{color:var(--navy)}
</style>
</head>
<body>

<section class="page page--front">
  <div class="hero" role="img" aria-label="Night view of the Helsinki harbour with a tall ship and lit buildings"></div>
  <div class="event-mark"><span class="event-mark__dot"></span><span class="event-mark__name">KVRD2014</span></div>

  <header class="title-band">
    <h1>FIRST CALL FOR PAPERS</h1>
    <h2>Electronic Assembly and Microsystem Research (KVRD) Conference</h2>
  </header>

  <div class="event-date">September 15 – 18, 2014, Helsinki, Finland</div>
  <div class="event-url">www.kvrd2014.example (http://192.0.2.18)</div>
  <p class="intro">It is our pleasure to announce that the 5th KVRD Conference, the premier European event in the field of microelectronics packaging and integration, will be held 15th – 18th of September, 2014, at Harborline Hall in Helsinki, Finland. This international event brings together both academics as well as the industry leaders to discuss and debate the state-of-the-art and the future trends in packaging and integration technologies. KVRD provides a perfect opportunity to hear the latest news and developments in the field. So mark the dates down on your calendar now!</p>

  <div class="columns">
    <div class="col">
      <div class="tab">Background</div>
      <p>The KVRD conference is organized by OQJU-LDSW in association with uNOLT-Europe. The 2014 event continues the line of prestigious events since the birth of the conference in Leipzig, Germany in 2006, and followed by Bristol, Hamburg, and Rotterdam every even year. KVRD is truly an international event as people from 26 countries attended the 4th KVRD conference in Rotterdam.</p>
      <div class="tab">Call for Papers</div>
      <p>KVRD 2014 seeks original papers describing research in all areas of electronic packaging. You are invited to submit abstracts that provide non-commercial information on new developments and knowledge in the areas including, but not limited to examples given for each technical track:</p>
      <div class="topic">3D integration and embedding technologies:</div>
      <p>Challenges and solutions in 3D integration, embedded, and wafer level packaging, micro-bonding, TSVs, TEVs, advanced substrates and interposers, etc.</p>
      <div class="topic">Advanced and Emerging Technologies:</div>
      <p>allotropes of carbon (CNTs, graphene, DLC, etc.), emerging packaging concepts and technologies, microfluidics, bio-electronics, flexible and stretchable electronics, etc.</p>
    </div>
    <div class="col">
      <div class="topic">Assembly and Manufacturing Technology:</div>
      <p>novel assembly technologies, manufacturing aspects to novel packaging, wafer level processing, etc.</p>
      <div class="topic">Materials for Interconnect and Packaging:</div>
      <p>new materials and processing – e.g. phase change, piezoelectric, self-organizing, and memory materials, dielectric materials, advanced interconnection metallurgies, etc.</p>
      <div class="topic">MEMS/NEMS packaging:</div>
      <p>challenges and solutions in processing, integration, and packaging, new packaging approaches, bonding technologies: wafer bonding, micro-bonding, etc.</p>
      <div class="topic">Modeling in Electronics:</div>
      <p>Thermal, mechanical, and electrical modeling and experimental verifications, signal and power integrity, etc.</p>
      <div class="topic">Optoelectronic Packaging:</div>
      <p>Fiber optical interconnects, optical sensors, LEDs and other photonic devices, optical chip-scale and heterogeneous integration, lasers, etc.</p>
      <div class="topic">Power Electronic Packaging:</div>
      <p>high performance packaging (low RDS(on); high temperature), Si power diode and thyristor devices, wide bandgap power semiconductor devices (e.g. SiC, GaN, GaAs), novel cooling solutions, etc.</p>
    </div>
  </div>

  <footer class="partners">
    <span class="partner"><span class="partner__mark"></span>Brenmoor University</span>
    <span class="partner">LDSW</span>
    <span class="partner">OQJU</span>
    <span class="partner">uNOLT</span>
  </footer>
</section>

<section class="page page--back">
  <div class="columns back-top">
    <div class="col">
      <div class="topic">Printable electronics:</div>
      <p>printed/jetted (transparent) conductors, touch sensors, screens and displays (e.g. OLED), paper electronics, 3D printing, PV, etc.</p>
      <div class="topic" style="margin-top:12px">Reliability:</div>
      <p>challenges at different levels of investigations (system, board, package and joint), characterization and test methods, interconnection reliability; characterization, and next generation/novel packaging reliability.</p>
      <div class="tab" style="margin-top:30px">Abstract Submission</div>
      <p>You are invited to submit a 300-500 word abstract that describes the scope, content and key points of your proposed paper. Abstracts must include results and graphics. The official language of all presentations is English. Please visit www.kvrd2014.example to find more information and to upload your abstract. Submission of abstracts will be opened 1.1.2014 and the abstracts are due 28.2.2014. All abstracts must be submitted electronically at the conference web site.<br>All submitted abstracts will be reviewed by the committee to ensure a high-quality conference. Authors will be notified of paper acceptance with instructions for publication by 18.4.2014.<br>If you have any questions, please contact: Lucien Marvaud, Program Chair of the 5th KVRD, via email (firstname.lastname@lab-nord.example)</p>
    </div>
    <div class="col">
      <div class="tab" style="margin-top:0">Publication of Papers</div>
      <p>All oral and poster presentation papers will be included in the conference proceedings and made available at the OQJU Archive Digital Library (archive.oqju.example).<br><br>In order to be included in OQJU Archive the paper must be original and not previously published, and avoid inclusion of commercial content.</p>
      <div class="tab">Best Paper Awards</div>
      <p>KVRD will select the best paper presentation. The author(s) will receive a personalized KVRD award and share a check for EUR 1 000.<br>KVRD will select the best poster whose author(s) will receive a personalized KVRD award and share a check for EUR 1 000.</p>
      <div class="tab">Professional Development Courses</div>
      <p>In addition to abstracts for papers we call proposals from individuals interested in teaching educational professional development courses (4 hours) on the topics described in the Call for Papers. Proposal should be submitted to Lucien Marvaud, the Program Chair of the 5th KVRD, via email (firstname.lastname@lab-nord.example) also by 28.2.2014.</p>
      <div class="tab">Important Dates:</div>
      <ul class="dates">
        <li>Abstract submission: <b>28.2.2014</b></li>
        <li>Notification of acceptance: <b>18.4.2014</b></li>
        <li>Papers in the final form: <b>20.6.2014</b></li>
      </ul>
    </div>
  </div>

  <div class="band-welcome">We look forward to welcoming you to the fifth OQJU-LDSW Electronics<br>Assembly and Microsystem Research Conference KVRD 2014 in Helsinki!</div>

  <div class="chairs">
    <div class="chair"><div class="chair__name">Aino Lehtivaara</div><div class="chair__role">General Chair</div></div>
    <div class="chair"><div class="chair__name">Eero Halsti</div><div class="chair__role">Executive Chair</div></div>
    <div class="chair"><div class="chair__name">Lucien Marvaud</div><div class="chair__role">Program Chair</div></div>
  </div>

  <div class="cityscape" role="img" aria-label="Faded grey Helsinki waterfront skyline with the cathedral dome"></div>

  <footer class="partners">
    <span class="partner"><span class="partner__mark"></span>Brenmoor University</span>
    <span class="partner">LDSW</span>
    <span class="partner">OQJU</span>
    <span class="partner">uNOLT</span>
  </footer>
</section>

</body>
</html>
```